Copper Gavel Auctions business card design with existing logo

Looking for a sleek and sexy design using our current logo

Contact Information for Business Card

Name, address, email, phone, website. Marcus Delvane 418 Birchmont Road Suite 200C Fenwick NY 11093 Copperbidhouse.net (631)582-4067

```html
<!DOCTYPE html>
<html lang="en">
<head>
<meta charset="utf-8">
<title>Copper Gavel Auctions – Business Card</title>
<link href="https://fonts.googleapis.com/css2?family=Arimo:wght@400;700&display=swap" rel="stylesheet">
<style>
  :root{
    --bg:#1d1f22;
    --card:#303133;
    --card-edge:#d0161d;
    --red:#e0161f;
    --blue:#1f4fa0;
    --white:#f2f2f2;
    --muted:#d9d9d9;
    --ghost:#3a3b3e;
  }
  *{margin:0;padding:0;box-sizing:border-box}
  html,body{width:1200px;height:900px;overflow:hidden;background:var(--bg);font-family:"Arimo",Arial,sans-serif}
  .stage{position:relative;width:1200px;height:900px}
  .card{
    position:absolute;left:260px;width:680px;height:389px;
    background:var(--card);border-radius:22px;overflow:hidden;
    box-shadow:0 6px 0 var(--card-edge),0 18px 30px rgba(0,0,0,.5);
  }
  .card--back{top:40px}
  .card--front{top:470px}
  .ghost-mark{position:absolute}
  .card--back .ghost-mark{left:40px;top:30px}
  .card--front .ghost-mark{left:250px;top:120px}

  .brand-name{color:var(--red);font-weight:700;text-transform:uppercase;line-height:1.1}
  .brand-sub{color:var(--red);font-weight:700;text-transform:uppercase;line-height:1.1}
  .brand-tagline{color:var(--blue);font-weight:700;text-transform:uppercase}

  .back-brand{position:absolute;right:50px;top:140px;text-align:right}
  .back-brand .brand-name{font-size:32px;letter-spacing:2px}
  .back-brand .brand-sub{font-size:22px;letter-spacing:6px;margin-top:4px}
  .back-brand .brand-tagline{font-size:15px;letter-spacing:5px;margin-top:8px}

  .front-brand{position:absolute;left:40px;top:32px;display:flex;align-items:center;gap:14px}
  .front-brand .dot{width:44px;height:44px;border-radius:50%;background:var(--red);flex:none}
  .front-brand .brand-name{font-size:22px;letter-spacing:1.5px}
  .front-brand .brand-sub{font-size:15px;letter-spacing:5px;margin-top:3px}
  .front-brand .brand-tagline{font-size:11px;letter-spacing:3.5px;margin-top:5px}

  .contact-list{position:absolute;left:40px;top:150px;list-style:none}
  .contact-list li{display:flex;align-items:center;gap:12px;color:var(--muted);font-size:15px;margin-bottom:12px}
  .contact-list svg{width:16px;height:16px;flex:none}

  .holder-name{position:absolute;right:40px;top:44px;color:var(--white);font-weight:700;font-size:24px;letter-spacing:1px;text-transform:uppercase;white-space:nowrap}
  .red-tab{position:absolute;right:0;top:44px;width:14px;height:30px;background:var(--red)}

  .address{position:absolute;right:40px;bottom:40px;text-align:right;color:var(--white);font-size:17px;line-height:1.45;font-style:normal}
</style>
</head>
<body>
<main class="stage">

  <section class="card card--back" aria-label="Card back">
    <svg class="ghost-mark" width="330" height="330" viewBox="0 0 330 330" aria-hidden="true">
      <circle cx="165" cy="165" r="150" fill="none" stroke="var(--ghost)" stroke-width="26"/>
    </svg>
    <div class="back-brand">
      <div class="brand-name">Copper Gavel</div>
      <div class="brand-sub">Auctions</div>
      <div class="brand-tagline">Buy·Sell·Consign</div>
    </div>
  </section>

  <section class="card card--front" aria-label="Card front">
    <svg class="ghost-mark" width="240" height="240" viewBox="0 0 240 240" aria-hidden="true">
      <circle cx="120" cy="120" r="105" fill="none" stroke="var(--ghost)" stroke-width="20"/>
    </svg>

    <div class="front-brand">
      <span class="dot"></span>
      <div>
        <div class="brand-name">Copper Gavel</div>
        <div class="brand-sub">Auctions</div>
        <div class="brand-tagline">Buy·Sell·Consign</div>
      </div>
    </div>

    <ul class="contact-list">
      <li>
        <svg viewBox="0 0 16 16" aria-hidden="true"><path fill="var(--blue)" d="M3 1h3l1.5 4-2 1.3a9 9 0 0 0 4.2 4.2L11 8.5l4 1.5v3a2 2 0 0 1-2 2A12 12 0 0 1 1 3a2 2 0 0 1 2-2z"/></svg>
        (631)582-4067
      </li>
      <li>
        <svg viewBox="0 0 16 16" aria-hidden="true"><circle cx="8" cy="8" r="6.5" fill="none" stroke="var(--blue)" stroke-width="1.6"/><path d="M1.5 8h13M8 1.5c-3 3.5-3 9.5 0 13M8 1.5c3 3.5 3 9.5 0 13" fill="none" stroke="var(--blue)" stroke-width="1.2"/></svg>
        www.Copperbidhouse.net
      </li>
      <li>
        <svg viewBox="0 0 16 16" aria-hidden="true"><rect x="1" y="3" width="14" height="10" rx="1.5" fill="var(--blue)"/><path d="M1.5 4l6.5 5 6.5-5" fill="none" stroke="var(--card)" stroke-width="1.3"/></svg>
        Marcus@Copperbidhouse.net
      </li>
    </ul>

    <h1 class="holder-name">Marcus Delvane</h1>
    <span class="red-tab"></span>

    <address class="address">
      418 Birchmont Road<br>
      Suite 200C<br>
      Fenwick NY 11093
    </address>
  </section>

</main>
</body>
</html>
```